German Headhunter/ HR Consultancy needs Business Cards Design

We need a business Card Design for our Company in Stuttgart. We are specialized as Headhunter/ HR Consultancy in Placement of specialist and managers in permanent employment. Please refer to our business logo.

```html
<!DOCTYPE html>
<html lang="de">
<head>
<meta charset="utf-8">
<title>Kernwerk Personalberatung – Visitenkarten</title>
<link rel="stylesheet" href="https://fonts.googleapis.com/css2?family=Montserrat:wght@400;600;700&display=swap">
<style>
  :root {
    --brand-blue: #3a55a0;
    --card-white: #ffffff;
    --page-bg: #f4f5f8;
    --rule-grey: #9a9a9a;
    --text-blue: #3a55a0;
  }
  * { box-sizing: border-box; margin: 0; padding: 0; }
  html, body { width: 958px; height: 1200px; overflow: hidden; }
  body {
    background: var(--page-bg);
    font-family: "Montserrat", sans-serif;
    position: relative;
  }
  .card {
    position: absolute;
    top: 480px;
    width: 425px;
    height: 240px;
  }
  .card-front {
    left: 42px;
    background: var(--brand-blue);
    box-shadow: 0 4px 14px rgba(0,0,0,0.12);
  }
  .card-back {
    left: 491px;
    background: var(--card-white);
    border: 1px solid var(--brand-blue);
    box-shadow: 0 4px 14px rgba(0,0,0,0.08);
  }
  .wordmark {
    position: absolute;
    display: flex;
    align-items: center;
    gap: 12px;
    font-weight: 700;
    line-height: 1;
    text-transform: uppercase;
  }
  .wordmark-square { display: block; flex: none; }
  .wordmark-text span { display: block; }
  .card-front .wordmark {
    left: 80px; top: 96px; color: var(--card-white);
  }
  .card-front .wordmark-name { font-size: 26px; letter-spacing: 1px; }
  .card-front .wordmark-sub { font-size: 12px; letter-spacing: 0.6px; margin-top: 4px; }
  .card-back .wordmark {
    left: 24px; top: 168px; color: var(--text-blue); gap: 8px;
  }
  .card-back .wordmark-name { font-size: 17px; letter-spacing: 0.6px; }
  .card-back .wordmark-sub { font-size: 8px; letter-spacing: 0.3px; margin-top: 2px; }
  .person {
    position: absolute;
    left: 240px; top: 16px;
    padding-left: 10px;
    border-left: 2px solid var(--rule-grey);
    color: var(--text-blue);
    font-size: 12px;
    line-height: 1.45;
  }
  .person-name { font-weight: 700; }
  .contact-list {
    position: absolute;
    left: 240px; top: 149px;
    list-style: none;
    color: var(--text-blue);
    font-size: 12px;
    line-height: 22px;
  }
  .contact-list li { display: flex; align-items: center; gap: 6px; }
  .contact-list svg { width: 9px; height: 9px; fill: var(--rule-grey); flex: none; }
  .tagline-band {
    position: absolute;
    left: -1px; right: -1px; bottom: -1px;
    height: 19px;
    background: var(--brand-blue);
    color: var(--card-white);
    font-size: 8px;
    font-weight: 600;
    text-align: center;
    line-height: 19px;
    white-space: nowrap;
  }
</style>
</head>
<body>

<section class="card card-front" aria-label="Visitenkarte Vorderseite">
  <div class="wordmark">
    <svg class="wordmark-square" width="26" height="26" viewBox="0 0 26 26" aria-hidden="true"><rect width="26" height="26" fill="#ffffff"/></svg>
    <div class="wordmark-text">
      <span class="wordmark-name">Kernwerk</span>
      <span class="wordmark-sub">Personalberatung</span>
    </div>
  </div>
</section>

<section class="card card-back" aria-label="Visitenkarte Rückseite">
  <div class="person">
    <div class="person-name">Lena Hartmann</div>
    <div class="person-role">Managing Director</div>
  </div>

  <ul class="contact-list">
    <li><svg viewBox="0 0 24 24" aria-hidden="true"><path d="M6.6 10.8a15.1 15.1 0 0 0 6.6 6.6l2.2-2.2a1 1 0 0 1 1-.25 11.4 11.4 0 0 0 3.6.57 1 1 0 0 1 1 1V20a1 1 0 0 1-1 1A17 17 0 0 1 3 4a1 1 0 0 1 1-1h3.5a1 1 0 0 1 1 1c0 1.25.2 2.45.57 3.57a1 1 0 0 1-.25 1z"/></svg>555-214-0386</li>
    <li><svg viewBox="0 0 24 24" aria-hidden="true"><path d="M2 5h20v14H2z M3 6l9 7 9-7" /></svg>lena@kernwerk.com</li>
    <li><svg viewBox="0 0 24 24" aria-hidden="true"><path d="M12 2a10 10 0 1 0 0 20 10 10 0 0 0 0-20zm0 2c1 1.3 1.8 3 2.1 5H9.9C10.2 7 11 5.3 12 4zM4.3 11h3.6a16 16 0 0 0 0 2H4.3a8 8 0 0 1 0-2zm5.6 0h4.2a14 14 0 0 1 0 2H9.9a14 14 0 0 1 0-2zm6.2 0h3.6a8 8 0 0 1 0 2h-3.6a16 16 0 0 0 0-2zM9.9 15h4.2c-.3 2-1.1 3.7-2.1 5-1-1.3-1.8-3-2.1-5z"/></svg>www.kernwerk.com</li>
  </ul>

  <div class="wordmark">
    <svg class="wordmark-square" width="18" height="18" viewBox="0 0 18 18" aria-hidden="true"><rect width="18" height="18" fill="#3a55a0"/></svg>
    <div class="wordmark-text">
      <span class="wordmark-name">Kernwerk</span>
      <span class="wordmark-sub">Personalberatung</span>
    </div>
  </div>

  <div class="tagline-band">Lorem ipsum dolor sit amet, consectetur adipiscing elit, sed do eiusmod</div>
</section>

</body>
</html>
```